Trying to create a web site off this static page

I am trying to create a seperate web site for this specific page. https://brolandathletics.com/hire-a-star/ I am still trying to figure out the domain name, for now, I will use Gold Roster as the name. I want to use the same pictures, but much more eye catching. Help me come up with something nice, something i can use to market to my thousands of customers. Maybe some flash. Something dramatic. I have some more content that I would like to add as well, but in the meantime, lets see what you come up with. Good luck and thanks
Updates

Some of these are really great. I may extend this for a few days... Please is the pictures from the Broland Athletics web site, but I want to make a few changes.... I want the name of the site changes to LuxeHours.com and as far as columns and tabs on the site, These are the tabs that I want. Please work with these and make the changes.

Our Talent

Past Client Experiences

ABout Us ( Our Philosophy)

Our Process

Ideas

Business Opportunities/ Warm Introductions

For the front page, I would like this content added in

FRONT PAGE Use this tag line somewhere "Where Dreams Become Luxe Experiences
Exclusive talent. Tailored events. Memories that last a lifetime."

Welcome to Luxe Hours

Where unforgettable moments are made.

At Luxe Hours, we connect individuals, businesses, and organizations with the world’s most recognizable athletes, entertainers, and celebrities. Whether it’s a private celebration, a corporate event, or a once-in-a-lifetime experience, our team specializes in making the impossible possible.

What We Do

Celebrity Bookings – From iconic musicians to legendary athletes, we secure top-tier talent for parties, concerts, and corporate functions.

Corporate Engagements – Motivate, inspire, and entertain your team with appearances from world-class speakers and sports legends.

Private Experiences – Fishing trips with Grand Gridiron Final champions, golf outings with All-Stars, tequila tastings with Hall of Famers—our clients have done it all.

University & Charity Events – Elevate your fundraiser, gala, or campus program with star power that draws attention and delivers impact.

VIP Appearances – From sitting courtside at the Showcase Classic with an PBL legend to sparring with Rick Dunmore, no dream is too big.

Why Choose Luxe Hours?

Exclusive Access – We work directly with celebrities and their management teams to deliver authentic, unforgettable experiences.

Proven Track Record – From Summit 400 companies to private clients, we’ve orchestrated events with some of the most famous names in the world.

Custom Experiences – Every event is unique. We tailor each booking to fit your vision, budget, and audience.

Confidential & Professional – Our clients trust us to deliver world-class experiences with complete discretion and flawless execution.

Let’s Make It Happen

Whether you’re planning a corporate retreat, a milestone celebration, or a private experience you’ll never forget, LuxeHours.com is your partner in making it extraordinary.

👉 If you can dream it, we can make it happen.

```html
<!DOCTYPE html>
<html lang="en">
<head>
<meta charset="utf-8">
<title>Luxe Hours – Where Dreams Become Luxe Experiences</title>
<link rel="stylesheet" href="https://fonts.googleapis.com/css2?family=Oswald:wght@500;600;700&family=Poppins:wght@400;500;600&display=swap">
<style>
:root{
  --red:#d9252a;
  --red-dark:#b81d22;
  --ink:#1c1c1c;
  --text:#444;
  --muted:#666;
  --grey-bg:#f2f2f2;
  --pink-bg:#fdf1f2;
  --white:#fff;
  --footer:#1e1e1e;
}
*{box-sizing:border-box;margin:0;padding:0}
html,body{width:1200px;height:5017px;overflow:hidden}
body{font-family:"Poppins",sans-serif;color:var(--text);background:var(--white);position:relative}
.abs{position:absolute}
.heading{font-family:"Oswald",sans-serif;font-weight:600;color:var(--ink);text-transform:uppercase;letter-spacing:.3px}
.heading em{font-style:normal;color:var(--red)}
.btn{position:absolute;display:flex;align-items:center;justify-content:center;gap:8px;font-weight:600;font-size:12px;text-transform:uppercase;border-radius:24px;letter-spacing:.3px}
.btn-red{background:var(--red);color:var(--white)}
.btn-white{background:var(--white);color:var(--red)}
.ph{position:absolute}

/* header */
.site-header{position:absolute;left:0;top:0;width:1200px;height:94px;background:var(--white)}
.brand{position:absolute;left:140px;top:28px;display:flex;align-items:center;gap:10px;font-weight:600;font-size:26px;color:var(--ink)}
.brand .dot{width:22px;height:22px;background:var(--red);border-radius:50%}
.call{position:absolute;left:600px;top:22px;display:flex;align-items:center;gap:12px}
.call .ic{width:44px;height:44px;border-radius:50%;background:var(--red);display:flex;align-items:center;justify-content:center}
.call small{display:block;font-size:11px;letter-spacing:2px;color:var(--muted)}
.call strong{display:block;font-size:21px;color:var(--ink);font-weight:600;letter-spacing:.5px}
.main-nav{position:absolute;left:0;top:94px;width:1200px;height:46px;background:#111;border-bottom:3px solid var(--red);display:flex;align-items:center;padding-left:140px}
.main-nav a{color:var(--white);font-size:11.5px;font-weight:500;text-transform:uppercase;text-decoration:none;height:43px;display:flex;align-items:center;padding:0 27px;position:relative}
.main-nav a+a::before{content:"";position:absolute;left:0;top:16px;height:12px;border-left:1px solid #555}
.main-nav a.active{background:var(--red)}

/* hero */
.hero{position:absolute;left:0;top:140px;width:1200px;height:560px;overflow:hidden;
  background:
    radial-gradient(ellipse 260px 200px at 18% 12%,rgba(255,170,90,.85),transparent 70%),
    radial-gradient(ellipse 300px 220px at 82% 18%,rgba(255,120,70,.8),transparent 70%),
    radial-gradient(ellipse 380px 260px at 50% 8%,rgba(255,220,180,.55),transparent 70%),
    radial-gradient(ellipse 220px 180px at 8% 60%,rgba(90,120,255,.55),transparent 70%),
    radial-gradient(ellipse 240px 200px at 95% 55%,rgba(240,60,140,.6),transparent 70%),
    radial-gradient(ellipse 500px 260px at 50% 95%,rgba(20,8,14,.95),transparent 75%),
    linear-gradient(180deg,#7a2a3a 0%,#4a1a3a 45%,#1c0c16 100%)}
.hero::after{content:"";position:absolute;inset:0;background:linear-gradient(180deg,rgba(0,0,0,.25) 0%,rgba(0,0,0,.05) 45%,rgba(0,0,0,.35) 100%)}
.hero-text{position:absolute;left:0;top:52px;width:1200px;text-align:center;color:var(--white);z-index:1}
.hero-text .kicker{font-size:20px;letter-spacing:1px;text-transform:uppercase}
.hero-text h1{font-family:"Oswald",sans-serif;font-weight:600;font-size:48px;line-height:1.2;margin-top:4px}
.hero-text p{font-size:17px;margin-top:6px}
.hero .btn{z-index:1}
.scroll-down{position:absolute;left:564px;top:664px;width:72px;height:72px;border-radius:50%;background:var(--white);box-shadow:0 4px 12px rgba(0,0,0,.15);display:flex;align-items:center;justify-content:center}

/* welcome */
.welcome h2{position:absolute;left:140px;top:832px;font-size:30px}
.welcome .lead{position:absolute;left:140px;top:876px;font-size:14px;color:var(--ink)}
.welcome .body{position:absolute;left:140px;top:928px;width:410px;font-size:12.5px;line-height:1.75;color:var(--text)}
.photo{border:4px solid #fff;box-shadow:0 6px 16px rgba(0,0,0,.22)}

/* what we do */
.what{position:absolute;left:0;top:1282px;width:1200px;height:793px;background:var(--grey-bg)}
.sec-title{position:absolute;left:0;width:1200px;text-align:center}
.sec-title h2{font-size:30px}
.sec-title p{font-size:13.5px;margin-top:6px;color:var(--text)}
.sec-title .rule{width:80px;height:2px;background:var(--red);margin:10px auto 0}
.svc{position:absolute;width:240px}
.svc h3{color:var(--red);font-size:14px;font-weight:600;margin-bottom:6px}
.svc p{font-size:11.5px;line-height:1.8;color:var(--text)}
.svc.left{text-align:right}
.svc-ic{position:absolute;width:68px;height:68px;border-radius:50%;display:flex;align-items:center;justify-content:center}
.svc-ic.dark{background:#333}
.svc-ic.red{background:var(--red)}

/* process */
.process{position:absolute;left:0;top:2075px;width:1200px;height:528px;background:linear-gradient(135deg,#dc3a3f,#c9151b)}
.step{position:absolute;width:260px;text-align:center;color:var(--white)}
.step h3{font-size:16px;font-weight:600;letter-spacing:.3px}
.step p{font-size:13.5px;line-height:1.75;margin-top:6px}
.step-ic{position:absolute;width:84px;height:84px;border-radius:50%;background:var(--white);display:flex;align-items:center;justify-content:center}

/* why choose */
.why h2{position:absolute;left:134px;top:2686px;font-size:30px}
.why .lead{position:absolute;left:134px;top:2732px;font-size:13.5px;color:var(--ink)}
.card{position:absolute;top:2797px;width:215px;height:288px;border:1px solid #ddd;background:var(--white);text-align:center}
.card .ph{left:0;top:0;width:213px;height:142px}
.card h3{position:absolute;left:8px;right:8px;top:158px;color:var(--red);font-size:13px;font-weight:600;text-transform:uppercase;line-height:1.6}
.card p{position:absolute;left:14px;right:14px;font-size:11px;line-height:1.75;color:var(--text)}

/* testimonials */
.reviews{position:absolute;left:0;top:3168px;width:1200px;height:654px;background:var(--pink-bg)}
.review{position:absolute;top:217px;width:282px;height:330px;background:var(--white);border-radius:6px;box-shadow:0 4px 14px rgba(0,0,0,.06);text-align:center}
.review .stars{position:absolute;left:58px;top:32px;display:flex;gap:6px;align-items:center}
.review .g{width:24px;height:24px;border-radius:50%;background:#e6e6e6;margin-right:6px}
.review p{position:absolute;left:28px;right:28px;top:84px;font-size:11px;line-height:2.05;color:var(--text)}
.review hr{position:absolute;left:28px;right:28px;top:228px;border:0;border-top:1px solid #e3e3e3}
.review .name{position:absolute;left:0;right:0;top:244px;font-size:14.5px;font-weight:500;color:var(--ink)}
.review .role{position:absolute;left:0;right:0;top:272px;font-size:11px;color:var(--text)}
.review .avatar{position:absolute;left:113px;top:302px;width:56px;height:56px;border-radius:50%;border:3px solid var(--white);box-shadow:0 2px 6px rgba(0,0,0,.15);background:radial-gradient(circle at 50% 35%,#d9c3b0 0 28%,transparent 30%),linear-gradient(180deg,#e9eef5 0%,#e9eef5 55%,#2c3a56 56%,#1e2a40 100%)}

/* ideas */
.idea{position:absolute;top:4018px;width:248px;height:352px;overflow:hidden}
.idea .ph{left:0;top:0;width:248px;height:352px}
.idea::after{content:"";position:absolute;left:0;right:0;bottom:0;height:150px;background:linear-gradient(180deg,transparent,rgba(0,0,0,.75))}
.idea span{position:absolute;left:28px;right:28px;bottom:22px;z-index:1;text-align:center;color:var(--white);font-family:"Oswald",sans-serif;font-weight:600;font-size:18px;line-height:1.45;text-transform:uppercase;letter-spacing:.4px}
.dots{position:absolute;left:566px;top:4398px;display:flex;gap:8px}
.dots i{width:7px;height:7px;border-radius:50%;background:#ccc;display:block}
.dots i.on{background:var(--red)}

/* footer */
.site-footer{position:absolute;left:0;top:4560px;width:1200px;height:457px;color:#ddd;
  background:radial-gradient(ellipse 500px 300px at 20% 40%,rgba(80,60,60,.35),transparent 70%),radial-gradient(ellipse 500px 300px at 80% 60%,rgba(70,70,80,.35),transparent 70%),var(--footer)}
.cta{position:absolute;left:141px;top:4484px;width:917px;height:132px;background:linear-gradient(135deg,#de3b40,#c8161c);border-radius:10px;color:var(--white)}
.cta .ic{position:absolute;left:30px;top:42px;width:50px;height:50px;border-radius:50%;background:var(--white);display:flex;align-items:center;justify-content:center}
.cta h2{position:absolute;left:104px;top:28px;font-family:"Oswald",sans-serif;font-weight:600;font-size:28px;text-transform:uppercase;color:var(--white)}
.cta p{position:absolute;left:104px;top:72px;width:400px;font-size:12px;line-height:1.7}
.foot-brand{position:absolute;left:124px;top:100px;width:226px;height:95px;background:#000;display:flex;align-items:center;justify-content:center;gap:10px;font-weight:600;font-size:26px;color:var(--white)}
.foot-brand .dot{width:20px;height:20px;border-radius:50%;background:var(--red)}
.foot-about{position:absolute;left:124px;top:203px;width:240px;font-size:12px;line-height:1.8}
.follow{position:absolute;left:124px;top:260px;display:flex;align-items:center;gap:9px;font-size:12px}
.follow i{width:20px;height:20px;border-radius:50%;background:#3a3a3a;display:block}
.follow i.r{background:var(--red)}
.foot-col{position:absolute;top:124px}
.foot-col h4{font-size:16px;font-weight:500;color:var(--white);margin-bottom:16px}
.foot-col ul{list-style:none}
.foot-col li{font-size:11.5px;margin-bottom:13px}
.foot-col li::before{content:"•";margin-right:7px}
.foot-col .lbl{color:var(--red);font-size:12px}
.foot-col .val{font-size:12.5px;line-height:1.7;color:var(--white);margin-bottom:8px}
.subscribe{position:absolute;left:795px;top:120px;width:278px;height:200px;background:rgba(50,50,50,.8);border-radius:8px;padding:24px 18px}
.subscribe h4{font-size:16px;font-weight:500;color:var(--white)}
.subscribe p{font-size:11.5px;line-height:1.8;margin-top:10px}
.subscribe .field{margin-top:14px;width:216px;height:36px;border-radius:18px;background:var(--white);color:#999;font-size:11px;display:flex;align-items:center;justify-content:space-between;padding:0 16px}
.subscribe .go{margin-top:14px;width:152px;height:36px;border-radius:18px;background:var(--red);color:var(--white);font-size:12px;display:flex;align-items:center;justify-content:space-between;padding:0 22px}
.copyright{position:absolute;left:0;top:408px;width:1200px;border-top:1px solid #333;padding-top:18px;text-align:center;font-size:11px}
</style>
</head>
<body>

<header class="site-header">
  <div class="brand"><span class="dot"></span>Luxe Hours</div>
  <div class="call">
    <div class="ic"><svg width="20" height="20" viewBox="0 0 24 24" fill="#fff"><path d="M6.6 10.8a15 15 0 0 0 6.6 6.6l2.2-2.2c.3-.3.7-.4 1-.2 1.1.4 2.3.6 3.6.6.6 0 1 .4 1 1V20c0 .6-.4 1-1 1A17 17 0 0 1 3 4c0-.6.4-1 1-1h3.5c.6 0 1 .4 1 1 0 1.3.2 2.5.6 3.6.1.3 0 .7-.2 1z"/></svg></div>
    <div><small>CALL US TODAY</small><strong>(555) 210-4830</strong></div>
  </div>
  <div class="btn btn-red" style="left:874px;top:24px;width:183px;height:44px;border-radius:3px;font-size:11.5px">Get Started Today</div>
</header>

<nav class="main-nav">
  <a class="active">Our Talent</a>
  <a>Past Client Experiences</a>
  <a>About Us</a>
  <a>Our Process</a>
  <a>Ideas</a>
  <a>Business Opportunities</a>
</nav>

<section class="hero" role="img" aria-label="Concert crowd with raised hands under warm stage lights">
  <div class="hero-text">
    <div class="kicker">Where Dreams Become</div>
    <h1>LUXE EXPERIENCES</h1>
    <p>Exclusive talent. Tailored events. Memories that last a lifetime.</p>
  </div>
  <div class="btn btn-red" style="left:505px;top:190px;width:190px;height:44px;border-radius:3px;font-size:11.5px">Get Started Today</div>
</section>
<div class="scroll-down"><svg width="16" height="16" viewBox="0 0 16 16" fill="none" stroke="#333" stroke-width="1.8"><path d="M4 3l4 4 4-4M4 9l4 4 4-4"/></svg></div>

<section class="welcome">
  <h2 class="heading">Welcome to <em>Luxe Hours</em></h2>
  <div class="lead">Where unforgettable moments are made.</div>
  <p class="body">At Luxe Hours, we connect individuals, businesses, and organizations with the world’s most recognizable athletes, entertainers, and celebrities. Whether it’s a private celebration, a corporate event, or a once-in-a-lifetime experience, our team specializes in making the impossible possible.</p>
  <div class="btn btn-red" style="left:140px;top:1098px;width:184px;height:42px">Meet Our Team <span>»</span></div>
  <div class="ph photo" role="img" aria-label="Client photo with a celebrity guest at an event" style="left:633px;top:778px;width:203px;height:236px;background:radial-gradient(ellipse 120px 90px at 30% 25%,#efe6d6,transparent 70%),radial-gradient(ellipse 110px 140px at 70% 70%,#6f7a8c,transparent 70%),linear-gradient(160deg,#c7b49a 0%,#8a7862 50%,#3f3a38 100%)"></div>
  <div class="ph photo" role="img" aria-label="Client photo with a sports legend" style="left:847px;top:836px;width:203px;height:310px;background:radial-gradient(ellipse 120px 180px at 28% 55%,#2a2a2e,transparent 70%),radial-gradient(ellipse 100px 120px at 75% 60%,#4b5060,transparent 70%),linear-gradient(160deg,#b7b2ab 0%,#7b7874 45%,#2e2f33 100%)"></div>
  <div class="ph photo" role="img" aria-label="Group photo of guests at a celebrity appearance" style="left:665px;top:1022px;width:173px;height:173px;background:radial-gradient(ellipse 90px 70px at 50% 20%,#c8d4ea,transparent 70%),radial-gradient(ellipse 110px 90px at 50% 85%,#2a4aa0,transparent 70%),linear-gradient(160deg,#6a7fa6 0%,#33456e 60%,#1a2238 100%)"></div>
</section>

<section class="what">
  <div class="sec-title" style="top:82px">
    <h2 class="heading">What <em>we do</em></h2>
    <p>Tailored experiences for unforgettable memories</p>
    <div class="rule"></div>
  </div>

  <svg class="abs" style="left:446px;top:214px" width="308" height="308" viewBox="0 0 308 308">
    <circle cx="154" cy="154" r="151" fill="none" stroke="#d9252a" stroke-width="2" stroke-dasharray="6 6"/>
    <circle cx="154" cy="154" r="132" fill="#f1e1e1"/>
    <text x="154" y="167" text-anchor="middle" font-family="Oswald, sans-serif" font-weight="700" font-size="38" fill="#1c1c1c">LUXE HOURS</text>
  </svg>

  <div class="svc left" style="left:82px;top:252px"><h3>Celebrity Bookings</h3><p>From iconic musicians to legendary athletes, we secure top-tier talent for parties, concerts, and corporate functions.</p></div>
  <div class="svc-ic dark" style="left:344px;top:252px"><svg width="30" height="30" viewBox="0 0 24 24" fill="none" stroke="#fff" stroke-width="1.5"><path d="M12 3l2.2 4.5 5 .7-3.6 3.5.9 5-4.5-2.4-4.5 2.4.9-5L4.8 8.2l5-.7z"/></svg></div>

  <div class="svc left" style="left:82px;top:434px"><h3>Corporate Engagement</h3><p>Motivate, inspire, and entertain your team with appearances from world-class speakers and sports legends.</p></div>
  <div class="svc-ic red" style="left:344px;top:439px"><svg width="30" height="30" viewBox="0 0 24 24" fill="none" stroke="#fff" stroke-width="1.5"><circle cx="12" cy="12" r="8"/><circle cx="12" cy="12" r="3"/></svg></div>

  <div class="svc-ic dark" style="left:781px;top:252px"><svg width="30" height="30" viewBox="0 0 24 24" fill="none" stroke="#fff" stroke-width="1.5"><circle cx="7" cy="9" r="2.5"/><circle cx="17" cy="9" r="2.5"/><circle cx="12" cy="7" r="2.5"/><path d="M3 19c0-3 2-5 4-5s4 2 5 2 3-2 5-2 4 2 4 5"/></svg></div>
  <div class="svc" style="left:871px;top:252px;width:260px"><h3>Private Experiences</h3><p>Fishing trips with Grand Gridiron Final champions, golf outings with All-Stars, tequila with Hall of Famers—our have done it all.</p></div>

  <div class="svc-ic red" style="left:781px;top:439px"><svg width="30" height="30" viewBox="0 0 24 24" fill="none" stroke="#fff" stroke-width="1.5"><rect x="4" y="5" width="16" height="14" rx="2"/><path d="M8 12l3 3 5-6"/></svg></div>
  <div class="svc" style="left:871px;top:434px;width:260px"><h3>VIP Appearances</h3><p>From sitting courtside at the Showcase Classic with an PBL legend to sparring with Rick Dunmore, no dream is too big.</p></div>

  <div class="svc-ic dark" style="left:566px;top:557px"><svg width="30" height="30" viewBox="0 0 24 24" fill="none" stroke="#fff" stroke-width="1.5"><circle cx="12" cy="12" r="8"/><path d="M12 8v8M8 12h8"/></svg></div>
  <div class="svc" style="left:400px;top:644px;width:400px;text-align:center"><h3>University &amp; Charity Events</h3><p>Elevate your fundraiser, gala, or campus program with star power that draws and delivers impact.</p></div>
</section>

<section class="process">
  <div class="sec-title" style="top:82px">
    <h2 class="heading" style="color:#fff">Our Process – How we make Luxe Hours happen</h2>
    <div class="rule" style="background:#fff"></div>
  </div>
  <svg class="abs" style="left:300px;top:180px" width="600" height="70" viewBox="0 0 600 70" fill="none" stroke="#fff" stroke-width="1.3" stroke-dasharray="4 4"><path d="M20 40 Q110 5 230 15"/><path d="M370 45 Q480 65 580 30"/><path d="M130 6l6 4-6 4M470 48l6 4-6 4" stroke-dasharray="0"/></svg>
  <div class="step-ic" style="left:220px;top:174px"><svg width="38" height="38" viewBox="0 0 24 24" fill="none" stroke="#d9252a" stroke-width="1.5"><rect x="3" y="5" width="14" height="14" rx="1.5"/><path d="M3 9h14M7 3v4M13 3v4"/><circle cx="18" cy="17" r="4" fill="#fff"/><path d="M18 15v2l1.5 1"/></svg></div>
  <div class="step-ic" style="left:558px;top:174px"><svg width="38" height="38" viewBox="0 0 24 24" fill="none" stroke="#d9252a" stroke-width="1.5"><circle cx="12" cy="7" r="3"/><path d="M6 20c0-4 3-6 6-6s6 2 6 6"/><path d="M3 11h4M17 11h4"/></svg></div>
  <div class="step-ic" style="left:895px;top:174px"><svg width="38" height="38" viewBox="0 0 24 24" fill="none" stroke="#d9252a" stroke-width="1.5"><path d="M7 21V11l4-7c1.5 0 2 1 2 2l-1 4h6c1 0 2 1 1.8 2l-1.5 7c-.2.8-1 1.5-2 1.5z"/><path d="M3 11h4v10H3z"/></svg></div>
  <div class="step" style="left:132px;top:276px"><h3>Planning &amp; Customization</h3><p>There are many variations of passages of Lorem Ipsum available, but majority</p></div>
  <div class="step" style="left:470px;top:276px"><h3>Booking &amp; Coordination</h3><p>There are many variations of passages of Lorem Ipsum available, but majority</p></div>
  <div class="step" style="left:807px;top:276px"><h3>Follow-up &amp; Feedback</h3><p>There are many variations of passages of Lorem Ipsum available, but majority</p></div>
  <div class="btn btn-white" style="left:504px;top:407px;width:191px;height:42px">Meet Our Team <span>»</span></div>
</section>

<section class="why">
  <h2 class="heading">Why choose <em>Luxe Hours?</em></h2>
  <div class="lead">Exclusive talent. Tailored events. Memories that last a lifetime.</div>
  <div class="btn btn-red" style="left:882px;top:2720px;width:182px;height:40px">Meet Our Team <span>»</span></div>

  <div class="card" style="left:134px"><div class="ph" role="img" aria-label="Business handshake at a meeting" style="background:radial-gradient(ellipse 90px 60px at 55% 45%,#d8d2ca,transparent 70%),radial-gradient(ellipse 110px 80px at 20% 80%,#1c1c1e,transparent 70%),linear-gradient(135deg,#9c968e 0%,#55504a 55%,#232120 100%)"></div><h3>Exclusive Access</h3><p style="top:184px">We work directly with celebrities &amp; their management teams to deliver authentic, unforgettable experiences.</p></div>
  <div class="card" style="left:373px"><div class="ph" role="img" aria-label="Team reviewing plans at a laptop" style="background:radial-gradient(ellipse 80px 70px at 40% 35%,#e2d2c0,transparent 70%),radial-gradient(ellipse 100px 70px at 70% 80%,#3c3028,transparent 70%),linear-gradient(135deg,#b8a48c 0%,#7a6450 55%,#3a2e26 100%)"></div><h3>Proven Track Record</h3><p style="top:184px">From Summit 400 companies to private clients, we’ve orchestrated events with some of the most famous names in the world.</p></div>
  <div class="card" style="left:612px"><div class="ph" role="img" aria-label="Planning notes spread on a table" style="background:radial-gradient(ellipse 70px 50px at 45% 55%,#f0a25a,transparent 70%),radial-gradient(ellipse 60px 40px at 70% 35%,#f4c08a,transparent 70%),linear-gradient(135deg,#efe4d6 0%,#c9a27e 55%,#7e5a3e 100%)"></div><h3>Custom Experiences</h3><p style="top:184px">Every event is unique. We tailor each booking to fit your vision, budget, and audience.</p></div>
  <div class="card" style="left:850px"><div class="ph" role="img" aria-label="Professionals reviewing documents in an office" style="background:radial-gradient(ellipse 80px 70px at 70% 45%,#f2f2f0,transparent 70%),radial-gradient(ellipse 90px 90px at 25% 60%,#1e2330,transparent 70%),linear-gradient(135deg,#c8ccd0 0%,#7a808a 50%,#2a2e36 100%)"></div><h3>Confidential and Professional</h3><p style="top:206px">Our clients trust us to deliver world-class experiences with complete discretion and flawless execution.</p></div>
</section>

<section class="reviews">
  <div class="sec-title" style="top:82px">
    <h2 class="heading">Past Client <em>Experiences</em></h2>
    <p style="width:640px;margin:8px auto 0;line-height:1.75">Our extended network features celebrated athletes and personalities such as Dana Whitfield, Marcus Holloway, Tommy Verlaine</p>
  </div>
  <div class="review" style="left:141px">
    <div class="stars"><i class="g"></i><svg width="130" height="20" viewBox="0 0 130 20" fill="#f5a623"><g id="star5"><path d="M10 1l2.7 5.6 6.1.9-4.4 4.3 1 6.1L10 15l-5.4 2.9 1-6.1L1.2 7.5l6.1-.9z"/><path transform="translate(27 0)" d="M10 1l2.7 5.6 6.1.9-4.4 4.3 1 6.1L10 15l-5.4 2.9 1-6.1L1.2 7.5l6.1-.9z"/><path transform="translate(54 0)" d="M10 1l2.7 5.6 6.1.9-4.4 4.3 1 6.1L10 15l-5.4 2.9 1-6.1L1.2 7.5l6.1-.9z"/><path transform="translate(81 0)" d="M10 1l2.7 5.6 6.1.9-4.4 4.3 1 6.1L10 15l-5.4 2.9 1-6.1L1.2 7.5l6.1-.9z"/><path transform="translate(108 0)" d="M10 1l2.7 5.6 6.1.9-4.4 4.3 1 6.1L10 15l-5.4 2.9 1-6.1L1.2 7.5l6.1-.9z"/></g></svg></div>
    <p>Lorem Ipsum Is Simply Dummy Text Of The Printing And Typesetting Industry. Lorem Ipsum Has Been The Industry's Standard Dummy Text Ever Since The 1500s, When An Unknown Printer Took</p>
    <hr><div class="name">Daniel Park</div><div class="role">Investment Director</div>
    <div class="avatar" role="img" aria-label="Client portrait"></div>
  </div>
  <div class="review" style="left:459px">
    <div class="stars"><i class="g"></i><svg width="130" height="20" viewBox="0 0 130 20" fill="#f5a623"><use href="#star5"/></svg></div>
    <p>Lorem Ipsum Is Simply Dummy Text Of The Printing And Typesetting Industry. Lorem Ipsum Has Been The Industry's Standard Dummy Text Ever Since The 1500s, When An Unknown Printer Took</p>
    <hr><div class="name">Owen Marsh</div><div class="role">Founder &amp; CEO of XYZ</div>
    <div class="avatar" role="img" aria-label="Client portrait"></div>
  </div>
  <div class="review" style="left:777px">
    <div class="stars"><i class="g"></i><svg width="130" height="20" viewBox="0 0 130 20" fill="#f5a623"><use href="#star5"/></svg></div>
    <p>Lorem Ipsum Is Simply Dummy Text Of The Printing And Typesetting Industry. Lorem Ipsum Has Been The Industry's Standard Dummy Text Ever Since The 1500s, When An Unknown Printer Took</p>
    <hr><div class="name">Lena Alvarez</div><div class="role">Property Owner</div>
    <div class="avatar" role="img" aria-label="Client portrait"></div>
  </div>
</section>

<section class="ideas">
  <div class="sec-title" style="top:3904px">
    <h2 class="heading">Ideas for your VIP <em>Experience</em></h2>
    <p>From the extraordinary to the once-in-a-lifetime.</p>
    <div class="rule"></div>
  </div>
  <div class="idea" style="left:197px"><div class="ph" role="img" aria-label="Players on an outdoor basketball court in autumn" style="background:radial-gradient(ellipse 140px 120px at 30% 20%,#d8a86a,transparent 70%),radial-gradient(ellipse 120px 100px at 80% 35%,#b86a3a,transparent 70%),radial-gradient(ellipse 90px 110px at 50% 60%,#d4552a,transparent 70%),linear-gradient(180deg,#a88a6c 0%,#6c4e3a 50%,#3a2a22 80%,#241a16 100%)"></div><span>Courtside at the Showcase Classic</span></div>
  <div class="idea" style="left:476px"><div class="ph" role="img" aria-label="Performer on stage facing a concert crowd" style="background:radial-gradient(ellipse 160px 90px at 50% 10%,#e8ecf4,transparent 70%),radial-gradient(ellipse 200px 80px at 50% 62%,#f0c070,transparent 70%),radial-gradient(ellipse 120px 160px at 15% 30%,#4a5468,transparent 70%),linear-gradient(180deg,#30343e 0%,#6e7280 40%,#5a4630 65%,#1c150e 100%)"></div><span>Exclusive Concert Backstage Pass</span></div>
  <div class="idea" style="left:755px"><div class="ph" role="img" aria-label="Golfer putting on a mountain course" style="background:radial-gradient(ellipse 160px 80px at 50% 5%,#e4ecf0,transparent 70%),radial-gradient(ellipse 200px 90px at 40% 30%,#6c7e7a,transparent 70%),radial-gradient(ellipse 160px 80px at 50% 75%,#9ab05a,transparent 70%),linear-gradient(180deg,#c2ccd2 0%,#72846c 35%,#55703a 65%,#3c5226 100%)"></div><span>Private Golf with Legends</span></div>
  <div class="dots"><i></i><i></i><i class="on"></i><i></i><i></i></div>
</section>

<footer class="site-footer" role="contentinfo">
  <div class="foot-brand"><span class="dot"></span>Luxe Hours</div>
  <p class="foot-about">Your trusted partner in commercial real estate and business sales.</p>
  <div class="follow">Follow Us : <i></i><i class="r"></i><i></i></div>
  <div class="foot-col" style="left:410px">
    <h4>Quick Links</h4>
    <ul><li>Our Talent</li><li>About Us</li><li>Our Process</li><li>Why Choose Us</li><li>Contact</li></ul>
  </div>
  <div class="foot-col" style="left:578px;width:200px">
    <h4>Contact Us</h4>
    <div class="lbl">Location</div><div class="val">Suite 12, 480 Harbor Ave<br>Westlake CA 90210</div>
    <div class="lbl">Phone Number :</div><div class="val">+(555) 210 4830</div>
    <div class="lbl">Email Address :</div><div class="val">info@goldroster.com</div>
  </div>
  <div class="subscribe">
    <h4>Stay in Touch</h4>
    <p>Subscribe to our newsletter for market updates and new property listings.</p>
    <div class="field">Email address <svg width="14" height="10" viewBox="0 0 14 10" fill="none" stroke="#999"><rect x=".5" y=".5" width="13" height="9"/><path d="M.5.5l6.5 5 6.5-5"/></svg></div>
    <div class="go">Subscribe <svg width="12" height="12" viewBox="0 0 12 12" fill="#fff"><path d="M1 1l10 5-10 5 2-5z"/></svg></div>
  </div>
  <div class="copyright">Copyright © Broland Athletics Group All Rights Reserved. Powered by Kestrel Marketing</div>
</footer>

<div class="cta">
  <div class="ic"><svg width="22" height="22" viewBox="0 0 24 24" fill="#d9252a"><path d="M6.6 10.8a15 15 0 0 0 6.6 6.6l2.2-2.2c.3-.3.7-.4 1-.2 1.1.4 2.3.6 3.6.6.6 0 1 .4 1 1V20c0 .6-.4 1-1 1A17 17 0 0 1 3 4c0-.6.4-1 1-1h3.5c.6 0 1 .4 1 1 0 1.3.2 2.5.6 3.6.1.3 0 .7-.2 1z"/></svg></div>
  <h2>Business Opportunities &amp; Partnerships</h2>
  <p>Short paragraph about collaboration, sponsorships, and corporate partnerships.</p>
  <div class="btn btn-white" style="left:690px;top:46px;width:190px;height:40px">Meet Our Team <span>»</span></div>
</div>

</body>
</html>
```